Business Card Design

I need a business card for company that is a limited company that was originally an off-road vehicle company (atv's side by sides snowmobiles and motorcycles) and I have recently sold the assets of the company that was operating under a different name and have become semi retired. I continue to do maintenance on these types of vehicles and also sell and install parts and accessories. Recently I have also contracted to a snowmobile club to operate their groomer to groom the snowmobile trails. I would like bright and bold colors.
Industry/Entity Type
Club
Contact Information for Business Card
KWT Holdings Ltd.
Marcus Ellery
780-555-0143

```html
<!DOCTYPE html>
<html lang="en">
<head>
<meta charset="UTF-8">
<title>KWT Holdings Ltd. — Business Card</title>
<link href="https://fonts.googleapis.com/css2?family=Ubuntu:wght@400;500;700&display=swap" rel="stylesheet">
<style>
  :root {
    --stage: #a3a3a3;
    --card-white: #ffffff;
    --plate-dark: #161616;
    --plate-mid: #2e2e2e;
    --brand-red: #d8262b;
    --brand-red-deep: #a9161b;
    --steel: #b9b9b9;
    --ink-light: #f2f2f2;
  }
  * { box-sizing: border-box; margin: 0; padding: 0; }
  html, body {
    width: 1200px; height: 900px; overflow: hidden;
    background: var(--stage);
    font-family: "Ubuntu", sans-serif;
  }
  .stage {
    width: 1200px; height: 900px;
    display: flex; align-items: center; justify-content: center; gap: 50px;
  }
  .card {
    width: 525px; height: 300px;
    border-radius: 24px; overflow: hidden; position: relative;
    box-shadow: 0 10px 24px rgba(0,0,0,.25);
  }
  .plate {
    background: radial-gradient(ellipse at 50% 40%, var(--plate-mid) 0%, var(--plate-dark) 75%);
  }

  /* front */
  .card-front { display: flex; flex-direction: column; }
  .front-top {
    background: var(--card-white);
    height: 150px;
    display: flex; flex-direction: column; align-items: center; justify-content: flex-end;
    padding-bottom: 12px;
  }
  .vehicle-lineup {
    width: 230px; height: 78px; border-radius: 10px;
    background: linear-gradient(90deg, #2b2b2b 0%, #c4252a 35%, #3a3a3a 55%, #d33035 78%, #e9e9e9 100%);
    margin-bottom: 6px;
  }
  .brand-name {
    color: var(--brand-red);
    font-weight: 700;
    font-size: 38px;
    line-height: 1;
    letter-spacing: .5px;
  }
  .band-red { height: 9px; background: var(--brand-red); }
  .band-steel { height: 4px; background: var(--steel); }
  .front-bottom {
    flex: 1;
    display: flex; flex-direction: column; align-items: center;
    padding-top: 14px;
  }
  .person-name { color: var(--brand-red); font-size: 25px; font-weight: 500; letter-spacing: .5px; }
  .contact { color: var(--ink-light); font-size: 21px; line-height: 1.2; text-align: center; margin-top: 16px; }
  .contact .email { font-size: 19px; }

  /* back */
  .card-back {
    display: flex; flex-direction: column; align-items: center;
    padding-top: 42px;
  }
  .card-back .vehicle-lineup { width: 220px; height: 74px; }
  .card-back .brand-name { font-size: 36px; }
  .credentials {
    list-style: none; text-align: center;
    color: var(--ink-light); font-size: 13.5px; line-height: 1.2; letter-spacing: .4px;
    text-transform: uppercase; margin-top: 24px;
  }
</style>
</head>
<body>
<main class="stage">
  <section class="card card-front" aria-label="Business card front">
    <div class="front-top">
      <div class="vehicle-lineup" role="img" aria-label="Photo of a motorcycle, an ATV and a snowmobile in red and black"></div>
      <div class="brand-name">KWT Holdings Ltd.</div>
    </div>
    <div class="band-red"></div>
    <div class="band-steel"></div>
    <div class="front-bottom plate">
      <div class="person-name">Marcus Ellery</div>
      <div class="contact">
        <div class="phone">780-555-0143</div>
        <div class="email">kwtholdings.43@example.com</div>
      </div>
    </div>
  </section>

  <section class="card card-back plate" aria-label="Business card back">
    <div class="vehicle-lineup" role="img" aria-label="Photo of a motorcycle, an ATV and a snowmobile in red and black"></div>
    <div class="brand-name">KWT Holdings Ltd.</div>
    <ul class="credentials">
      <li>Journeyman Automotive Technician Red Seal</li>
      <li>Journeyman Motorcycle Technician Red Seal</li>
      <li>Journeyman Partsperson</li>
      <li>Snowmobile Trail Groomer</li>
    </ul>
  </section>
</main>
</body>
</html>
```